Mobile app for checking bus arrival

I would like to make the UI much more beautiful and modern. The app is an app to check bus arrival in Singapore.
See here: https://apps.plorvex.net/store/apps/details?id=com.ridetk&hl=en

Based on the question from designers:

1. The first screen shows the favorite bus stop. Each item shows location / street, the top one is the location, second line is the street name. And the number is the bus stop code.

2. Please download the app and try bus stop code with 07589 or 10079, for example. It will bring you to the next screen.

3. The pencil allow you to select color theme, for the list item, and the header.

4. On the second screen, it will show up the list of bus route that available on that bus stop.

5. When you tap on one of them it will show you the 2 subsequent arrival time.

6. Each of the arrival time has the information of availability seats available, seats not available, no more space. (we can use green, yellow, red, respectively).

7. Each of the arrival time has the WAB indicator (Wheelchair availability). Show as icon is preferred.

7. KLT and DAVN are the bus provider in Singapore. 48 means the route /service no.

Requirements:
And check the attachment, see screen 3. I need to add information about the space availability, which has 3 state: seats available, seats not available, no more space. (we can use green, yellow, red, respectively).

Please advise how to show the information.

Target Market(s)

Students, age below 35

Industry/Entity Type

Vexora

Requirements
Must have
• The app currently has the capabilities to select color theme, checkout screen1. It's the button and the list item color.
Nice to have
• Please download the app to see all available colors, and make suggestion to have better color pallete.

```html
<!DOCTYPE html>
<html lang="en">
<head>
<meta charset="utf-8">
<title>Bus arrival – route list with seat availability</title>
<link rel="stylesheet" href="https://fonts.googleapis.com/css2?family=Roboto:wght@300;400;500&display=swap">
<style>
:root{
  --bg:#aaaaaa;
  --orange:#e64a19;
  --purple:#673ab7;
  --grey:#6b6b6b;
  --red:#d32f2f;
  --green:#1e9e0f;
  --yellow:#f7f400;
  --ink:#222;
  --black:#000;
  --white:#fff;
}
*{box-sizing:border-box;margin:0;padding:0}
html,body{width:1200px;height:700px;overflow:hidden}
body{background:var(--bg);font-family:'Roboto',sans-serif;position:relative}
.screen{position:absolute;top:13px;width:320px;height:674px;background:var(--white);overflow:hidden}
.screen--collapsed{left:15px}
.screen--expanded{left:407px}
.status-bar{position:absolute;top:0;left:0;right:0;height:22px;background:var(--black);color:var(--white);font-size:12px}
.status-bar .note{position:absolute;top:5px;width:12px;height:12px;background:var(--white);border-radius:2px}
.status-bar .clock{position:absolute;right:8px;top:4px}
.status-bar .sys{position:absolute;top:5px;width:10px;height:12px;background:var(--white);border-radius:1px}
.app-bar{position:absolute;top:22px;left:0;right:0;height:50px;background:var(--orange);color:var(--white)}
.app-bar .title{position:absolute;left:50px;top:13px;font-size:21px;font-weight:400}
.app-bar svg{position:absolute;top:13px}
.fav-row{position:absolute;top:72px;left:0;right:0;height:36px;background:var(--white);font-size:12px;color:#555}
.fav-row svg{position:absolute;left:10px;top:11px}
.fav-row .label{position:absolute;left:40px;top:11px}
.fav-row .stop{position:absolute;right:13px;top:10px;font-size:13px}
.route{position:absolute;left:0;width:320px;height:83px;border-bottom:1px solid var(--purple)}
.route .band{position:absolute;left:0;top:0;height:100%;width:320px;clip-path:polygon(0 0,100% 0,calc(100% - 13px) 100%,0 100%)}
.route.is-open .band{width:208px;clip-path:polygon(0 0,100% 0,calc(100% - 15px) 100%,0 100%)}
.band--klt-purple{background:var(--purple)}
.band--davn{background:var(--grey)}
.band--klt-red{background:var(--red)}
.route .operator{position:absolute;left:15px;top:28px;color:var(--white);font-size:22px}
.route .operator-sub{position:absolute;left:29px;top:62px;color:var(--white);font-size:9px}
.route .number{position:absolute;left:120px;width:80px;text-align:center;top:26px;color:var(--white);font-size:28px}
.route .number-sub{position:absolute;left:120px;width:80px;text-align:center;top:62px;color:var(--white);font-size:8px}
.route.is-open .number,.route.is-open .number-sub{left:66px}
.route .toggle{position:absolute;left:270px;top:33px}
.route.is-open .toggle{left:164px}
.seats{position:absolute;left:212px;top:24px;width:108px}
.badge{position:absolute;top:0;width:35px;height:33px;border-radius:4px;font-size:16px;display:flex;align-items:center;justify-content:center}
.badge--green{left:8px;background:var(--green);color:var(--white)}
.badge--yellow{left:59px;background:var(--yellow);color:var(--ink)}
.badge--red{background:var(--red);color:var(--white)}
.badge--red.first{left:8px}.badge--red.second{left:59px}
.seats .caption{position:absolute;top:38px;left:0;width:110px;text-align:center;font-size:8px;color:var(--ink)}
.nav-bar{position:absolute;bottom:0;left:0;right:0;height:42px;background:var(--black)}
.nav-bar svg{position:absolute;top:12px}
.gesture{position:absolute;border-radius:45% 45% 40% 40%;background:linear-gradient(#ffffff,#e6e6e6);border:2px solid #333}
.brand{position:absolute;left:915px;top:92px;width:120px;text-align:center;color:var(--white)}
.brand .mark{display:block;width:76px;height:76px;border-radius:50%;background:var(--white);margin:0 auto 8px}
.brand .name{font-size:18px;font-weight:400}
.legend-text{position:absolute;left:910px;font-size:22px;font-weight:300;color:var(--ink)}
.legend-badge{position:absolute;left:856px;width:46px;height:46px;background:var(--white);padding:5px}
.legend-badge span{display:flex;width:100%;height:100%;border-radius:4px;align-items:center;justify-content:center;font-size:15px}
</style>
</head>
<body>

<!-- Screen: route list collapsed -->
<section class="screen screen--collapsed">
  <div class="status-bar">
    <span class="note" style="left:8px"></span><span class="note" style="left:26px"></span><span class="note" style="left:44px"></span><span class="note" style="left:62px"></span><span class="note" style="left:80px"></span>
    <span class="sys" style="left:242px"></span><span class="sys" style="left:258px"></span><span class="sys" style="left:274px"></span>
    <span class="clock">6:18</span>
  </div>
  <header class="app-bar">
    <svg style="left:16px" width="18" height="24" viewBox="0 0 18 24"><path d="M17 12H3M9 5l-7 7 7 7" stroke="#fff" stroke-width="2" fill="none"/></svg>
    <span class="title">10079</span>
    <svg style="left:208px" width="24" height="24" viewBox="0 0 24 24"><path d="M12 2l3 7h7l-5.6 4.3 2.1 7.2L12 16.3 5.5 20.5l2.1-7.2L2 9h7z" stroke="#fff" stroke-width="2" fill="none"/></svg>
    <svg style="left:252px" width="24" height="24" viewBox="0 0 24 24"><path d="M19 12a7 7 0 1 1-2-5" stroke="#fff" stroke-width="2.4" fill="none"/><path d="M20 3v6h-6z" fill="#fff"/></svg>
    <svg style="left:296px" width="6" height="24" viewBox="0 0 6 24"><circle cx="3" cy="5" r="2" fill="#fff"/><circle cx="3" cy="12" r="2" fill="#fff"/><circle cx="3" cy="19" r="2" fill="#fff"/></svg>
  </header>
  <div class="fav-row">
    <svg width="16" height="16" viewBox="0 0 24 24"><path d="M12 2l3 7h7l-5.6 4.3 2.1 7.2L12 16.3 5.5 20.5l2.1-7.2L2 9h7z" fill="#888"/></svg>
    <span class="label">My Favorite</span><span class="stop">blk 201, jln merah</span>
  </div>

  <div class="route" style="top:109px"><div class="band band--klt-purple"></div><span class="operator">KLT</span><span class="operator-sub">bus</span><span class="number">130</span><span class="number-sub">route no.</span><svg class="toggle" width="14" height="16"><path d="M13 1v14L1 8z" fill="#fff"/></svg></div>
  <div class="route" style="top:195px"><div class="band band--davn"></div><span class="operator">DAVN</span><span class="operator-sub">bus</span><span class="number">960</span><span class="number-sub">route no.</span><svg class="toggle" width="14" height="16"><path d="M13 1v14L1 8z" fill="#fff"/></svg></div>
  <div class="route" style="top:282px"><div class="band band--klt-purple"></div><span class="operator">KLT</span><span class="operator-sub">bus</span><span class="number">2N</span><span class="number-sub">route no.</span><svg class="toggle" width="14" height="16"><path d="M13 1v14L1 8z" fill="#fff"/></svg></div>
  <div class="route" style="top:369px"><div class="band band--klt-red"></div><span class="operator">KLT</span><span class="operator-sub">bus</span><span class="number">57</span><span class="number-sub">route no.</span><svg class="toggle" width="14" height="16"><path d="M13 1v14L1 8z" fill="#fff"/></svg></div>
  <div class="route" style="top:456px"><div class="band band--davn"></div><span class="operator">DAVN</span><span class="operator-sub">bus</span><span class="number">851</span><span class="number-sub">route no.</span><svg class="toggle" width="14" height="16"><path d="M13 1v14L1 8z" fill="#fff"/></svg></div>
  <div class="route" style="top:543px"><div class="band band--klt-red"></div><span class="operator">KLT</span><span class="operator-sub">bus</span><span class="number">48</span><span class="number-sub">route no.</span><svg class="toggle" width="14" height="16"><path d="M13 1v14L1 8z" fill="#fff"/></svg></div>

  <div class="gesture" role="img" aria-label="Hand gesture: swipe left or right" style="left:188px;top:160px;width:36px;height:52px"></div>
  <div class="gesture" role="img" aria-label="Hand gesture: tap arrow" style="left:272px;top:340px;width:34px;height:50px"></div>

  <nav class="nav-bar">
    <svg style="left:62px" width="18" height="18"><path d="M16 2v14L3 9z" stroke="#fff" stroke-width="1.6" fill="none"/></svg>
    <svg style="left:150px" width="18" height="18"><circle cx="9" cy="9" r="7" stroke="#fff" stroke-width="1.6" fill="none"/></svg>
    <svg style="left:240px" width="18" height="18"><rect x="2" y="2" width="13" height="13" stroke="#fff" stroke-width="1.6" fill="none"/></svg>
  </nav>
</section>

<!-- Screen: route list with seat availability -->
<section class="screen screen--expanded">
  <div class="status-bar">
    <span class="note" style="left:8px"></span><span class="note" style="left:26px"></span><span class="note" style="left:44px"></span><span class="note" style="left:62px"></span><span class="note" style="left:80px"></span>
    <span class="sys" style="left:242px"></span><span class="sys" style="left:258px"></span><span class="sys" style="left:274px"></span>
    <span class="clock">6:18</span>
  </div>
  <header class="app-bar">
    <svg style="left:16px" width="18" height="24" viewBox="0 0 18 24"><path d="M17 12H3M9 5l-7 7 7 7" stroke="#fff" stroke-width="2" fill="none"/></svg>
    <span class="title">10079</span>
    <svg style="left:208px" width="24" height="24" viewBox="0 0 24 24"><path d="M12 2l3 7h7l-5.6 4.3 2.1 7.2L12 16.3 5.5 20.5l2.1-7.2L2 9h7z" stroke="#fff" stroke-width="2" fill="none"/></svg>
    <svg style="left:252px" width="24" height="24" viewBox="0 0 24 24"><path d="M19 12a7 7 0 1 1-2-5" stroke="#fff" stroke-width="2.4" fill="none"/><path d="M20 3v6h-6z" fill="#fff"/></svg>
    <svg style="left:296px" width="6" height="24" viewBox="0 0 6 24"><circle cx="3" cy="5" r="2" fill="#fff"/><circle cx="3" cy="12" r="2" fill="#fff"/><circle cx="3" cy="19" r="2" fill="#fff"/></svg>
  </header>
  <div class="fav-row">
    <svg width="16" height="16" viewBox="0 0 24 24"><path d="M12 2l3 7h7l-5.6 4.3 2.1 7.2L12 16.3 5.5 20.5l2.1-7.2L2 9h7z" fill="#888"/></svg>
    <span class="label">My Favorite</span><span class="stop">blk 201, jln merah</span>
  </div>

  <div class="route is-open" style="top:109px"><div class="band band--klt-purple"></div><span class="operator">KLT</span><span class="operator-sub">bus</span><span class="number">130</span><span class="number-sub">route no.</span><svg class="toggle" width="14" height="16"><path d="M1 1v14l12-7z" fill="#fff"/></svg>
    <div class="seats"><span class="badge badge--green">10</span><span class="badge badge--yellow">18</span><span class="caption">open seats</span></div></div>
  <div class="route is-open" style="top:195px"><div class="band band--davn"></div><span class="operator">DAVN</span><span class="operator-sub">bus</span><span class="number">960</span><span class="number-sub">route no.</span><svg class="toggle" width="14" height="16"><path d="M1 1v14l12-7z" fill="#fff"/></svg>
    <div class="seats"><span class="badge badge--red first">0</span><span class="badge badge--red second">0</span><span class="caption">no more space</span></div></div>
  <div class="route" style="top:282px"><div class="band band--klt-purple"></div><span class="operator">KLT</span><span class="operator-sub">bus</span><span class="number">2N</span><span class="number-sub">route no.</span><svg class="toggle" width="14" height="16"><path d="M13 1v14L1 8z" fill="#fff"/></svg></div>
  <div class="route is-open" style="top:369px"><div class="band band--klt-red"></div><span class="operator">KLT</span><span class="operator-sub">bus</span><span class="number">57</span><span class="number-sub">route no.</span><svg class="toggle" width="14" height="16"><path d="M1 1v14l12-7z" fill="#fff"/></svg>
    <div class="seats"><span class="badge badge--green">10</span><span class="badge badge--yellow">28</span><span class="caption">open seats</span></div></div>
  <div class="route" style="top:456px"><div class="band band--davn"></div><span class="operator">DAVN</span><span class="operator-sub">bus</span><span class="number">851</span><span class="number-sub">route no.</span><svg class="toggle" width="14" height="16"><path d="M13 1v14L1 8z" fill="#fff"/></svg></div>
  <div class="route is-open" style="top:543px"><div class="band band--klt-red"></div><span class="operator">KLT</span><span class="operator-sub">bus</span><span class="number">48</span><span class="number-sub">route no.</span><svg class="toggle" width="14" height="16"><path d="M1 1v14l12-7z" fill="#fff"/></svg>
    <div class="seats"><span class="badge badge--green">10</span><span class="badge badge--yellow">18</span><span class="caption">open seats</span></div></div>

  <div class="gesture" role="img" aria-label="Hand gesture: swipe left or right" style="left:40px;top:170px;width:36px;height:52px"></div>
  <div class="gesture" role="img" aria-label="Hand gesture: tap arrow" style="left:156px;top:428px;width:34px;height:50px"></div>

  <nav class="nav-bar">
    <svg style="left:62px" width="18" height="18"><path d="M16 2v14L3 9z" stroke="#fff" stroke-width="1.6" fill="none"/></svg>
    <svg style="left:150px" width="18" height="18"><circle cx="9" cy="9" r="7" stroke="#fff" stroke-width="1.6" fill="none"/></svg>
    <svg style="left:240px" width="18" height="18"><rect x="2" y="2" width="13" height="13" stroke="#fff" stroke-width="1.6" fill="none"/></svg>
  </nav>
</section>

<!-- Legend -->
<div class="brand"><span class="mark"></span><span class="name">Ridetk</span></div>

<div class="gesture" role="img" aria-label="Hand gesture: swipe left or right" style="left:856px;top:218px;width:36px;height:48px"></div>
<span class="legend-text" style="top:232px;left:908px">swipe left or right</span>

<div class="gesture" role="img" aria-label="Hand gesture: click arrow" style="left:858px;top:304px;width:34px;height:48px"></div>
<span class="legend-text" style="top:315px">click arrow</span>

<div class="legend-badge" style="top:396px"><span style="background:var(--red);color:var(--white)">0</span></div>
<span class="legend-text" style="top:405px;left:911px">no more space</span>

<div class="legend-badge" style="top:475px;left:858px"><span style="background:var(--yellow);color:var(--ink)">28</span></div>
<span class="legend-text" style="top:483px;left:914px">seats not available</span>

<div class="legend-badge" style="top:559px;left:860px"><span style="background:var(--green);color:var(--white)">10</span></div>
<span class="legend-text" style="top:567px;left:914px">seats available</span>

</body>
</html>
```